Investment website design - investing in mutual funds

I need a design of a website (only homepage for now) dedicated to investment in mutual funds. Attached is a mock up with all the elements the homepage design should contain. The homepage should contain a logo in the upper left corner, the domain the website will run on is www.perovalstrinka.cz , in the upper right corner there should be 2 buttons or links SIGN UP / SIGN IN. The bottom of the homepage should contain links to ABOUT US, FAQ, PRIVACY POLICY, CONTACT US.
Now the main elements on the homepage
1) Video that will explain how the investment works exactly, under this video we will have 3 illustrated icons like the ones attached (see 2nd attachement) that will show the potential investor what exactly they could get when investing with us (education for kids, happy life after they retire, regular monthly payment for the rest of their life).
2) On the right side next to the video we will have a calculator where a potential investor can play with the numbers, the investor can fill in the MONTHLY PAYMENT that he wants to invest regularly every month, the time frame of the investment - for how long he wants to invest. Once the potential investor selects those 2 variables we will calculate for him 2 options - either he can get a ONE TIME PAYOUT once he reaches his investment horizon or he can get a regular monthly payment for the rest of his life. Under the laculator there will be a button 'I want to invest ->'. The functionality of the calculator should be similar to the calculator that can be found here http://www.brodavbank.cz/brodav-podilove-fondy/ and https://felbo.cz/.
The design should look similar to https://felbo.cz/ (font, colors, logo). We prefer white background in the area where we have the video and calculator. We also like the design of www.tarvupo.com. Let me know if you have any questions.

```html
<!DOCTYPE html>
<html lang="en">
<head>
<meta charset="utf-8">
<title>Perovalstrinka – Mutual Fund Investing</title>
<link href="https://fonts.googleapis.com/css2?family=Lato:wght@400;700;900&display=swap" rel="stylesheet">
<style>
  :root {
    --teal: #2f8784;
    --teal-dark: #276f6d;
    --orange: #f6b44b;
    --orange-deep: #f5a623;
    --red: #e8553b;
    --page-bg: #f2f2f2;
    --panel-bg: #f6f6f6;
    --panel-border: #e4e4e4;
    --text-dark: #4a4a4a;
    --text-mid: #6b6b6b;
    --white: #ffffff;
    --track: #e2e2e2;
  }
  * { box-sizing: border-box; margin: 0; padding: 0; }
  html, body {
    width: 1200px; height: 1200px; overflow: hidden;
    background: var(--white);
    font-family: 'Lato', Arial, sans-serif;
  }
  .site {
    position: absolute; left: 0; top: 214px;
    width: 1200px; height: 772px;
    background: var(--page-bg);
  }
  /* Header */
  .site-header {
    position: absolute; left: 0; top: 0; width: 1200px; height: 100px;
    background: var(--teal);
  }
  .brand {
    position: absolute; left: 132px; top: 32px;
    font-weight: 900; font-size: 32px; color: var(--white); letter-spacing: 0.2px;
  }
  .main-nav a {
    position: absolute; top: 45px;
    font-size: 14px; font-weight: 700; color: var(--white); text-decoration: none;
  }
  .main-nav .is-active::after {
    content: ""; position: absolute; left: 0; right: 0; top: 50px; height: 5px;
    background: var(--orange-deep);
  }
  .auth-btn {
    position: absolute; top: 40px; width: 79px; height: 26px;
    border-radius: 2px; font-size: 14px; font-weight: 700; color: var(--white);
    display: flex; align-items: center; justify-content: center;
  }
  .auth-btn--up { left: 916px; background: var(--orange-deep); }
  .auth-btn--in { left: 1004px; background: var(--red); }

  /* Video */
  .video {
    position: absolute; left: 130px; top: 160px; width: 432px; height: 282px;
    background: linear-gradient(135deg, #ececec 0%, #e3e6ea 55%, #efe4cf 100%);
  }
  .video-controls {
    position: absolute; left: 0; bottom: 0; width: 432px; height: 14px;
    background: linear-gradient(#dcdcdc, #c9c9c9);
  }
  .video-time {
    position: absolute; left: 94px; top: 2px; font-size: 8px; letter-spacing: 1px;
    color: #333; font-weight: 700;
  }

  /* Benefits */
  .benefit { position: absolute; top: 512px; width: 130px; text-align: center; }
  .benefit-art { width: 84px; height: 68px; margin: 0 auto 20px; border-radius: 6px; }
  .benefit-label { font-size: 14px; line-height: 16px; color: var(--text-mid); }

  /* Calculator */
  .calculator {
    position: absolute; left: 608px; top: 163px; width: 479px; height: 509px;
    background: var(--panel-bg); border: 1px solid var(--panel-border);
  }
  .calc-bar {
    position: absolute; left: 16px; width: 447px; height: 46px;
    background: var(--orange);
    color: var(--white); font-size: 15px; font-weight: 700;
    display: flex; align-items: center; padding-left: 22px;
  }
  .calc-title {
    position: absolute; left: 16px; top: 87px;
    font-size: 20px; font-weight: 700; color: var(--text-dark);
  }
  .slider { position: absolute; left: 16px; top: 120px; }
  .slider-label { position: absolute; font-size: 15px; color: var(--text-mid); }
  .or-badge {
    position: absolute; left: 199px; top: 275px; width: 60px; height: 60px;
    border-radius: 50%; background: var(--teal);
    color: var(--white); font-size: 21px; font-weight: 900;
    display: flex; align-items: center; justify-content: center;
  }
  .invest-btn {
    position: absolute; left: 16px; top: 446px; width: 447px; height: 46px;
    background: var(--teal); color: var(--white);
    font-size: 17px; font-weight: 700;
    display: flex; align-items: center; justify-content: center; gap: 14px;
    box-shadow: 0 2px 0 var(--teal-dark);
  }

  /* Footer */
  .site-footer {
    position: absolute; left: 0; top: 721px; width: 1200px; height: 51px;
    background: var(--orange);
  }
  .footer-nav a {
    position: absolute; top: 18px;
    font-size: 14px; font-weight: 700; letter-spacing: 0.8px;
    color: var(--white); text-decoration: none;
  }
  .footer-sep { position: absolute; top: 12px; width: 1px; height: 28px; background: rgba(255,255,255,0.45); }
  .social { position: absolute; top: 15px; width: 20px; height: 20px; border-radius: 50%; background: var(--white); }
</style>
</head>
<body>
<div class="site">
  <header class="site-header">
    <div class="brand">Perovalstrinka</div>
    <nav class="main-nav">
      <a class="is-active" style="left:560px">ABOUT</a>
      <a style="left:631px">FAQ</a>
      <a style="left:682px">PRIVACY POLICY</a>
      <a style="left:814px">CONTACT</a>
    </nav>
    <div class="auth-btn auth-btn--up">SIGN UP</div>
    <div class="auth-btn auth-btn--in">SIGN IN</div>
  </header>

  <section class="video" role="img" aria-label="Explainer video still: a businessman presenting charts, a calculator and a purse of gold coins">
    <div class="video-controls">
      <svg width="432" height="14" viewBox="0 0 432 14">
        <polygon points="14,3 14,11 21,7" fill="#222"/>
        <polygon points="42,7 47,3 47,11" fill="#222"/><polygon points="37,7 42,3 42,11" fill="#222"/>
        <polygon points="66,3 66,11 71,7" fill="#222"/><polygon points="71,3 71,11 76,7" fill="#222"/>
        <line x1="156" y1="7" x2="382" y2="7" stroke="#999" stroke-width="2"/>
        <rect x="156" y="6" width="5" height="2" fill="#333"/>
        <rect x="394" y="3" width="8" height="8" fill="none" stroke="#222" stroke-width="1.5"/>
        <polygon points="414,5 417,5 421,2 421,12 417,9 414,9" fill="#222"/>
      </svg>
      <span class="video-time">0:01/0:40</span>
    </div>
  </section>

  <div class="benefit" style="left:174px">
    <div class="benefit-art" role="img" aria-label="Illustration of stacked books with a graduation cap" style="background:linear-gradient(#3d4a55,#e8874a)"></div>
    <div class="benefit-label">Education For<br>Kids</div>
  </div>
  <div class="benefit" style="left:316px">
    <div class="benefit-art" role="img" aria-label="Illustration of a person relaxing in a hammock chair" style="background:linear-gradient(#f2b441,#2f6f8f)"></div>
    <div class="benefit-label">Possive<br>Income</div>
  </div>
  <div class="benefit" style="left:446px">
    <div class="benefit-art" role="img" aria-label="Illustration of a retired golfer swinging a club" style="background:linear-gradient(#e9e9e9,#e0533a)"></div>
    <div class="benefit-label">Happy<br>Retirement</div>
  </div>

  <section class="calculator">
    <div class="calc-bar" style="top:17px">Regular Mounthly Invesment</div>
    <div class="calc-title">Lenght of Invesment</div>
    <div class="slider">
      <svg width="447" height="30" viewBox="0 0 447 30">
        <rect x="0" y="11" width="447" height="4" fill="var(--track)"/>
        <rect x="0" y="11" width="59" height="4" fill="var(--teal)"/>
        <rect x="0" y="11" width="3" height="14" fill="var(--teal)"/>
        <g fill="var(--track)">
          <rect x="118" y="11" width="2" height="12"/><rect x="179" y="11" width="2" height="12"/>
          <rect x="240" y="11" width="2" height="12"/><rect x="301" y="11" width="2" height="12"/>
          <rect x="362" y="11" width="2" height="12"/><rect x="444" y="11" width="3" height="12"/>
        </g>
        <polygon points="51,6 67,6 69,15 59,22 49,15" fill="var(--orange)"/>
      </svg>
      <span class="slider-label" style="left:-3px;top:32px">0</span>
      <span class="slider-label" style="left:55px;top:32px">8</span>
      <span class="slider-label" style="left:392px;top:30px">30 Year</span>
    </div>
    <div class="calc-bar" style="top:195px">One Time Payment</div>
    <div class="or-badge">OR</div>
    <div class="calc-bar" style="top:371px">Monthly Payment</div>
    <div class="invest-btn">I WANT TO INVEST
      <svg width="28" height="14" viewBox="0 0 28 14"><line x1="1" y1="7" x2="25" y2="7" stroke="#fff" stroke-width="2"/><polyline points="19,1 26,7 19,13" fill="none" stroke="#fff" stroke-width="2"/></svg>
    </div>
  </section>

  <footer class="site-footer">
    <nav class="footer-nav">
      <a style="left:182px">ABOUT US</a>
      <span class="footer-sep" style="left:271px"></span>
      <a style="left:285px">FAQ</a>
      <span class="footer-sep" style="left:329px"></span>
      <a style="left:343px">PRIVACY</a>
      <span class="footer-sep" style="left:414px"></span>
      <a style="left:427px">POLICY</a>
      <span class="footer-sep" style="left:492px"></span>
      <a style="left:505px">CONTACT</a>
    </nav>
    <span class="social" style="left:990px"></span>
    <span class="social" style="left:1020px"></span>
    <span class="social" style="left:1050px"></span>
    <span class="social" style="left:1080px"></span>
  </footer>
</div>
</body>
</html>
```